Invite Card (Ministers) (business cards used for personal invitation to our church)

I need a business card sized advertisement. The card is a replacement for the attached card only much much cooler. I do not want a image background but more of a vectored, flat look with advertising colors.

I have attached a new image of the couple to replace the old image and a new logo to replace the old logo.

I need a PSD with ALL of the layers un-merged & unlocked

The back of the card should carry the same information as the old card.

Use advertising color and a modern flat look and feel.

Target Market(s)

professional audience

Industry/Entity Type

Non-Profit

Contact Information for Business Card

The card is a replacement for the attached card only much much cooler. I do not want a image background but more of a vectored, flat look with advertising colors.

Font styles to use
Sans Serif

Requirements
Must have
• Must have new logo, new image of couple
Should not have
• graphical background

```html
<!DOCTYPE html>
<html lang="en">
<head>
<meta charset="utf-8">
<title>Grace Harbor Ministries – Invite Card</title>
<link rel="stylesheet" href="https://fonts.googleapis.com/css2?family=Montserrat:wght@400;600;700;800&display=swap">
<style>
  :root{
    --navy:#0d4a75;
    --teal:#0f8c9e;
    --gold:#f2c200;
    --mist:#d4e1ea;
    --white:#ffffff;
    --page:#ffffff;
    --text-font:"Montserrat", Arial, sans-serif;
  }
  *{margin:0;padding:0;box-sizing:border-box;}
  html,body{width:1200px;height:1200px;overflow:hidden;background:var(--page);}
  .canvas{position:relative;width:1200px;height:1200px;font-family:var(--text-font);}

  .card{position:absolute;top:444px;width:546px;height:312px;background:var(--white);overflow:hidden;
        box-shadow:0 3px 6px rgba(0,0,0,.28);}
  .card--front{left:40px;}
  .card--back{left:614px;}

  .band{position:absolute;left:0;right:0;top:72px;background:linear-gradient(180deg,var(--navy) 0%,var(--navy) 40%,var(--teal) 100%);
        border-top:3px solid var(--gold);}
  .card--front .band{height:130px;}
  .card--back .band{height:130px;}

  /* front */
  .portrait{position:absolute;left:0;top:0;width:372px;height:290px;
            background:linear-gradient(160deg,#6b6f7a 0%,#3a3d47 45%,#c9a3cf 100%);}
  .front-name{position:absolute;left:384px;top:86px;width:148px;text-align:right;color:var(--white);
              font-weight:800;font-size:24px;line-height:1.05;letter-spacing:.5px;}
  .footer-bar{position:absolute;left:0;right:0;bottom:0;height:22px;background:var(--navy);}
  .footer-bar__strip{position:absolute;left:0;top:0;width:380px;height:22px;background:var(--mist);}
  .pastor-name{position:absolute;left:30px;top:0;line-height:22px;font-size:13px;font-weight:700;color:var(--navy);}

  /* back */
  .invite-title{position:absolute;left:0;width:546px;top:38px;padding-left:150px;text-align:center;
                font-size:15px;font-weight:700;color:var(--navy);letter-spacing:.6px;}
  .back-name{position:absolute;left:30px;top:100px;width:190px;color:var(--white);font-weight:800;
             font-size:26px;line-height:1.05;letter-spacing:.5px;}
  .schedule{position:absolute;left:230px;top:92px;}
  .schedule__divider{position:absolute;left:75px;top:0;width:1px;height:96px;background:rgba(255,255,255,.45);}
  .schedule__row{position:absolute;left:0;width:280px;height:18px;line-height:18px;color:var(--white);font-size:13px;white-space:nowrap;}
  .schedule__time{position:absolute;right:216px;font-weight:400;}
  .schedule__day{position:absolute;left:86px;font-weight:700;}
  .contact{position:absolute;left:232px;top:209px;color:var(--navy);font-size:12.5px;line-height:21px;font-weight:400;}
  .back-strip{position:absolute;left:0;right:0;bottom:0;height:22px;
              background:linear-gradient(90deg,var(--mist) 0%,#b9cfdc 50%,var(--navy) 100%);}
</style>
</head>
<body>
<div class="canvas">

  <section class="card card--front" aria-label="Invite card front">
    <div class="band"></div>
    <div class="portrait" role="img" aria-label="Photo of the pastor couple, smiling, in purple and pink attire"></div>
    <div class="front-name">GRACE<br>HARBOR<br>MINISTRIES</div>
    <div class="footer-bar">
      <div class="footer-bar__strip"></div>
      <div class="pastor-name">PASTOR DANIEL &amp; RUTH WHITMORE</div>
    </div>
  </section>

  <section class="card card--back" aria-label="Invite card back">
    <div class="invite-title">YOUR ARE INVITED</div>
    <div class="band"></div>
    <div class="back-name">GRACE<br>HARBOR<br>MINISTRIES</div>
    <div class="schedule">
      <div class="schedule__divider"></div>
      <div class="schedule__row" style="top:5px"><span class="schedule__time">9:00 AM</span><span class="schedule__day">SUNDAY</span></div>
      <div class="schedule__row" style="top:38px"><span class="schedule__time">11:00 AM</span><span class="schedule__day">SUNDAY</span></div>
      <div class="schedule__row" style="top:71px"><span class="schedule__time">7:00 PM</span><span class="schedule__day">WED. BIBLE CLASS</span></div>
    </div>
    <div class="contact">
      GRACEHARBORMINISTRY.ORG<br>
      2240 W. CEDAR LANE - FAIRVIEW, TX 75069<br>
      1-800-555-0142
    </div>
    <div class="back-strip"></div>
  </section>

</div>
</body>
</html>
```